Revamping and duplicating of existing business card

We are a painting and decorating business based in London and need a couple of business cards made up for the following people.

1. Marla Penhallow
2. Toby Renwick

Measurements - 85 X 55 mm
Font: Blue highway
Colour: No idea! Would be great to have a pantone for the pink if possible?

I’ve attached all the logos and old artwork etc.
Here are the amendments I would definitely like...

1. Marla

format mobile number correctly: 07451 386 902

Add title: Decorator
Use: Penhallow Decorating Logo
Add twitter logo & @penhallowdecor
Add tradeverify logo
Add HFG Logo
Make it all look beautiful/revamp/tweak - whatever you think…

2. Toby

Decorator

07623 519 840
toby@penhallowdecorating.co.uk
Updates

Hello! Thanks so much for all your designs. This is such a great way to get these things done... Just to clarify, Please do not alter our logo at all. The 'splat' appears on our van, tshirts, quotes etc and is very much part of our branding. Colour scheme: Pink, black and white. Thanks Marla

Reason: Not 100% sold on any of the designs so far but very grateful for all the submissions. Keep it simple and quirky please. Thanks Marla

Industry/Entity Type

Painting

Requirements
Must have
• Pink & Black Colour scheme
Penhallow Decorating Logo
Blue Highway font

```html
<!DOCTYPE html>
<html lang="en">
<head>
<meta charset="utf-8">
<title>Penhallow Decorating – Marla, Decorator</title>
<link rel="stylesheet" href="https://fonts.googleapis.com/css2?family=Signika:wght@400;600;700&display=swap">
<style>
  :root {
    --ink: #000000;
    --paper: #ffffff;
    --pink: #d9196b;
    --pink-soft: #e0307c;
    --plum: #3a2128;
    --plum-soft: #4a2a33;
    --badge: #2b3a8c;
    --listing: #e03a3a;
  }
  html, body {
    margin: 0;
    padding: 0;
    width: 1200px;
    height: 777px;
    overflow: hidden;
    background: var(--ink);
  }
  .card {
    position: relative;
    width: 1200px;
    height: 777px;
    background: var(--ink);
    overflow: hidden;
    font-family: "Signika", "Trebuchet MS", sans-serif;
    color: var(--paper);
  }
  .card p, .card h1 { white-space: nowrap; }
  .card__art {
    position: absolute;
    inset: 0;
  }
  .brand {
    position: absolute;
    left: 24px;
    top: 18px;
    margin: 0;
    font-weight: 700;
    color: var(--ink);
    font-size: 104px;
    line-height: 100px;
    letter-spacing: -1px;
  }
  .person {
    position: absolute;
    right: 14px;
    top: 188px;
    text-align: right;
  }
  .person__name {
    margin: 0;
    font-weight: 600;
    font-size: 76px;
    line-height: 80px;
  }
  .person__role {
    margin: 0;
    font-weight: 600;
    font-size: 40px;
    line-height: 44px;
  }
  .contact {
    position: absolute;
    right: 14px;
    top: 428px;
    text-align: right;
    font-weight: 400;
  }
  .contact__phone {
    margin: 0;
    font-size: 52px;
    line-height: 62px;
  }
  .contact__email {
    margin: 0;
    font-size: 48px;
    line-height: 60px;
  }
  .members__label {
    position: absolute;
    left: 302px;
    top: 640px;
    margin: 0;
    font-size: 20px;
  }
  .members__listing {
    position: absolute;
    left: 164px;
    top: 668px;
    margin: 0;
    font-size: 58px;
    font-weight: 600;
    color: var(--listing);
    line-height: 70px;
  }
  .social__handle {
    position: absolute;
    right: 14px;
    top: 668px;
    margin: 0;
    font-size: 45px;
    font-weight: 400;
    line-height: 70px;
    text-align: right;
  }
</style>
</head>
<body>
<main class="card">
  <svg class="card__art" width="1200" height="777" viewBox="0 0 1200 777">
    <defs>
      <radialGradient id="pinkWash" cx="0.45" cy="0.4" r="0.7">
        <stop offset="0" stop-color="#e0307c"/>
        <stop offset="1" stop-color="#d9196b"/>
      </radialGradient>
      <radialGradient id="plumWash" cx="0.5" cy="0.45" r="0.7">
        <stop offset="0" stop-color="#4a2a33"/>
        <stop offset="1" stop-color="#3a2128"/>
      </radialGradient>
    </defs>
    <rect class="splash splash--plum" role="img" aria-label="Dark plum paint splash" x="335" y="130" width="383" height="490" rx="60" fill="url(#plumWash)"/>
    <rect class="splash splash--brand" role="img" aria-label="Pink paint splash behind the company name" x="0" y="0" width="575" height="560" rx="40" fill="url(#pinkWash)"/>
    <rect class="splash splash--name" role="img" aria-label="Small pink paint splash behind the name" x="860" y="148" width="222" height="245" rx="80" fill="url(#pinkWash)"/>
    <circle class="members__badge" cx="84" cy="703" r="58" fill="var(--badge)" stroke="var(--paper)" stroke-width="4"/>
    <rect class="social__mark" x="694" y="644" width="112" height="114" rx="14" fill="var(--pink)"/>
  </svg>

  <h1 class="brand">Penhallow<br>Decorating</h1>

  <section class="person">
    <p class="person__name">Marla</p>
    <p class="person__role">Decorator</p>
  </section>

  <section class="contact">
    <p class="contact__phone">07451 386 902</p>
    <p class="contact__email">Marla@penhallowdecorating.co.uk</p>
  </section>

  <p class="members__label">Proud members of</p>
  <p class="members__listing">tradeverify</p>

  <p class="social__handle">@penhallowdecor</p>
</main>
</body>
</html>
```